Screendesign für neue Website
Zielgruppe
Bauherren und alle die mal zum Architekten müssen.
Aufgabenstellung
Bei diesem Auftrag handelt es sich um die Erstellung eines Screendesigns für eine Website eines Archtiktenbüros.
Es wird daher ein Layout im PSD-Format erwartet, eine Umsetzung dessen in HTML wird nicht gefordert.

```html
<!DOCTYPE html>
<html lang="de">
<head>
<meta charset="utf-8">
<title>Planungsbüro Henrik Laube</title>
<link rel="stylesheet" href="https://fonts.googleapis.com/css2?family=Arimo:wght@400&display=swap">
<style>
  :root {
    --page-bg: #1b1b1b;
    --frame: #3b3b3b;
    --frame-edge: #555555;
    --content-bg: #ffffff;
    --brand-text: #ffffff;
    --headline: #3a3a3a;
    --menu-top: #3a3a3a;
    --menu-bottom: #262626;
    --menu-active-top: #555555;
    --menu-active-bottom: #444444;
    --menu-line: #4a4a4a;
    --menu-text: #8c8c8c;
    --footer-text: #6a6a6a;
    --accent-light: #d6edbd;
    --accent-mid: #a9d67c;
    --nav-dot: #cfcfcf;
  }
  * { margin: 0; padding: 0; box-sizing: border-box; }
  html, body {
    width: 1200px; height: 720px; overflow: hidden;
    background: var(--page-bg);
    font-family: "Arimo", Arial, sans-serif;
  }
  .canvas { position: relative; width: 1200px; height: 720px; }

  .brand-mark {
    position: absolute; left: 202px; top: 86px;
    width: 58px; height: 58px; background: var(--brand-text);
  }
  .brand-name {
    position: absolute; left: 202px; top: 148px;
    font-size: 14px; color: var(--brand-text); letter-spacing: -0.2px;
  }

  .frame {
    position: absolute; left: 195px; top: 174px;
    width: 810px; height: 412px;
    background: var(--frame);
    border: 1px solid var(--frame-edge);
  }
  .content {
    position: absolute; left: 7px; top: 5px;
    width: 794px; height: 401px;
    background: var(--content-bg); overflow: hidden;
  }
  .photo-band {
    position: absolute; left: 0; top: 0; width: 794px; height: 112px;
    display: flex;
  }
  .photo-band div { flex: 1; }
  .photo-band div:nth-child(1), .photo-band div:nth-child(4) { background: linear-gradient(180deg, #5e6f86 0%, #a88a6a 55%, #3d5a2e 100%); }
  .photo-band div:nth-child(2), .photo-band div:nth-child(5) { background: linear-gradient(180deg, #8fa2bd 0%, #e6e6e6 55%, #5b7a3a 100%); }
  .photo-band div:nth-child(3) { background: linear-gradient(180deg, #5c85b5 0%, #b98a62 50%, #4f7032 100%); }

  .slider-arrow {
    position: absolute; top: 229px; width: 16px; height: 16px;
    border-radius: 50%; background: var(--nav-dot);
    border: 1px solid #888;
  }
  .slider-arrow svg { display: block; }
  .slider-arrow.prev { left: 172px; }
  .slider-arrow.next { left: 1012px; }

  .main-nav {
    position: absolute; left: 681px; top: 292px; width: 157px;
    list-style: none;
    box-shadow: 0 3px 6px rgba(0,0,0,0.35);
  }
  .main-nav li {
    height: 38.5px; line-height: 38px;
    padding-left: 34px;
    font-size: 15px; color: var(--menu-text);
    background: linear-gradient(180deg, var(--menu-top), var(--menu-bottom));
    border-bottom: 1px solid var(--menu-line);
  }
  .main-nav li.active {
    background: linear-gradient(180deg, var(--menu-active-top), var(--menu-active-bottom));
  }

  .ornament-area {
    position: absolute;
    background: linear-gradient(135deg, var(--accent-light), var(--accent-mid));
  }
  .tagline {
    position: absolute; font-size: 20px; color: var(--headline);
    white-space: nowrap;
  }

  .imprint {
    position: absolute; left: 195px; top: 595px;
    font-size: 10px; color: var(--footer-text);
  }
</style>
</head>
<body>
<div class="canvas">
  <div class="brand-mark" aria-hidden="true"></div>
  <div class="brand-name">Planungsbüro Henrik Laube</div>

  <span class="slider-arrow prev" aria-label="Zurück">
    <svg width="14" height="14" viewBox="0 0 14 14"><path d="M8.5 4 L5 7 L8.5 10" fill="none" stroke="#555" stroke-width="1.5"/></svg>
  </span>
  <span class="slider-arrow next" aria-label="Weiter">
    <svg width="14" height="14" viewBox="0 0 14 14"><path d="M5.5 4 L9 7 L5.5 10" fill="none" stroke="#555" stroke-width="1.5"/></svg>
  </span>

  <div class="frame">
    <div class="content">
      <div class="photo-band" role="img" aria-label="Fotoleiste mit modernen Einfamilienhäusern">
        <div></div><div></div><div></div><div></div><div></div>
      </div>

      <div class="ornament-area" role="img" aria-label="Kleeblatt-Ornament" style="left:30px; top:134px; width:46px; height:44px;"></div>
      <div class="tagline" style="left:42px; top:146px;">Architekten schaffen</div>

      <div class="ornament-area" role="img" aria-label="Kleeblatt-Ornament" style="left:108px; top:199px; width:46px; height:44px;"></div>
      <div class="tagline" style="left:131px; top:211px;">Lebens - Raum</div>

      <div class="ornament-area" role="img" aria-label="Kleeblatt-Ornament" style="left:186px; top:265px; width:46px; height:44px;"></div>
      <div class="tagline" style="left:210px; top:277px;">Lebens - Traum</div>

      <div class="ornament-area" role="img" aria-label="Kleeblatt-Ornament" style="left:263px; top:331px; width:46px; height:44px;"></div>
      <div class="tagline" style="left:283px; top:343px;">Traum Haus</div>

      <div class="ornament-area" role="img" aria-label="Großes Kleeblatt-Ornament" style="left:698px; top:318px; width:88px; height:78px;"></div>
    </div>
  </div>

  <ul class="main-nav">
    <li>Unternehmen</li>
    <li class="active">Projekte</li>
    <li>Information</li>
    <li>Aktuelles</li>
    <li>Leistungen</li>
    <li>Kontakt</li>
  </ul>

  <div class="imprint">Impressum</div>
</div>
</body>
</html>
```